Property Services Company Needs a Brochure Design

Looking for a new brochure design for an existing property services company.

We provide a range of property services from, market research, real estate brokerage, valuation and appraisal, property development and other real estate consulting services.

We would like a fresh modern brochure design with good graphics and features. Our colours are white, blue and orange.

The design should communicate, attention to detail, superior service delivery and distinction in results.
Updates

I would like the brochure to be roughly about 20 pages.

Containing the following,

1) An introduction
2) Contents Page
2) What we do
3) Our Services
4) Agency & Brokerage
5) Real Estate Consulting
6) Market Research
7) Appraisal & Valuation
8) Project Management
9) Property Development

I would also like icons to represent items 4,5,6,7,8 & 9, they should be represented vertically on each of the pages from the contents page and highlighted individually on the pages that they represent.. i.e. on appraisal & valuation page, all six icons will be arranged vertically and the appraisal and valuations icon will be highlighted.

I will also like to have images that depict the services on the various pages.

I have some pages I think will flow which I will upload shortly.

Industry/Entity Type

Real Estate

Font styles to use
Serif

Colors
f78f20
0455a3

```html
<!DOCTYPE html>
<html lang="en">
<head>
<meta charset="utf-8">
<title>Harrowgate Property Services – Back Page &amp; Cover Page</title>
<link rel="stylesheet" href="https://fonts.googleapis.com/css2?family=Source+Sans+3:wght@400;600&family=Roboto+Condensed:wght@400;500&family=Nunito:wght@600;900&display=swap">
<style>
  :root {
    --orange: #f78f20;
    --blue: #0455a3;
    --headline-blue: #1c5aa8;
    --pale-blue: #bcd3ea;
    --white: #ffffff;
    --ink: #1d1d1d;
    --logo-grey: #4a4a5e;
    --stage: #2f241e;
  }
  * { margin: 0; padding: 0; box-sizing: border-box; }
  html, body {
    width: 1200px; height: 960px; overflow: hidden;
    background: var(--stage);
  }
  .spread {
    position: absolute; left: 50px; top: 95px;
    width: 1100px; height: 770px;
    display: flex;
  }
  .page { position: relative; width: 550px; height: 770px; overflow: hidden; }

  /* Back page */
  .back-panel {
    position: absolute; left: 0; top: 0; width: 307px; height: 770px;
    background: var(--orange);
  }
  .back-photo {
    position: absolute; left: 307px; top: 0; width: 188px; height: 770px;
    background: linear-gradient(180deg, #f4f4f4 0%, #e6e6e3 35%, #cfd3cc 60%, #a99a88 80%, #6d5f55 100%);
    border-left: 2px solid #555;
  }
  .back-edge {
    position: absolute; left: 495px; top: 0; width: 55px; height: 770px;
    background: linear-gradient(90deg, #f3d2a8 0 14px, #d6e3f0 14px 100%);
  }
  .brand {
    position: absolute; display: flex; align-items: flex-start; gap: 10px;
    font-family: "Source Sans 3", sans-serif; font-weight: 400;
  }
  .brand-mark { flex: none; }
  .brand-name { line-height: 1; }
  .brand-name .line-main { display: block; }
  .brand-name .line-sub { display: block; }
  .back-brand { left: 35px; top: 478px; color: var(--white); }
  .back-brand .brand-mark { width: 28px; height: 28px; background: var(--white); margin-top: 8px; }
  .back-brand .line-main { font-size: 40px; }
  .back-brand .line-sub { font-size: 14px; margin-top: 4px; padding-left: 24px; }

  .contact-list {
    position: absolute; left: 36px; top: 595px; width: 270px;
    list-style: none;
    font-family: "Roboto Condensed", sans-serif; font-size: 15px; color: var(--ink);
  }
  .contact-item { display: flex; gap: 9px; align-items: flex-start; margin-bottom: 11px; line-height: 1.1; }
  .contact-icon {
    flex: none; width: 21px; height: 21px; border: 1.5px solid var(--white);
    border-radius: 3px; display: flex; align-items: center; justify-content: center;
  }
  .contact-text.web { color: var(--headline-blue); }

  /* Cover page */
  .cover-art { position: absolute; inset: 0; }
  .cover-brand { left: 90px; top: 88px; color: var(--logo-grey); }
  .cover-brand .brand-mark { width: 30px; height: 30px; background: var(--blue); margin-top: 10px; }
  .cover-brand .line-main { font-size: 42px; }
  .cover-brand .line-sub { font-size: 15px; margin-top: 4px; padding-left: 26px; }
  .headline text {
    font-family: "Nunito", sans-serif; font-weight: 900; font-size: 42px;
    fill: var(--headline-blue); stroke: var(--white); stroke-width: 9px;
    stroke-linejoin: round; paint-order: stroke;
  }
  .headline text.connector { font-weight: 600; font-size: 38px; }
</style>
</head>
<body>
<main class="spread">

  <section class="page back-page" aria-label="Back page">
    <div class="back-panel"></div>
    <div class="back-photo" role="img" aria-label="Photo of two women in a bright living room looking at a property brochure"></div>
    <div class="back-edge"></div>

    <div class="brand back-brand">
      <span class="brand-mark"></span>
      <span class="brand-name">
        <span class="line-main">Harrowgate</span>
        <span class="line-sub">Property Services</span>
      </span>
    </div>

    <ul class="contact-list">
      <li class="contact-item">
        <span class="contact-icon">
          <svg width="12" height="14" viewBox="0 0 12 14"><path d="M6 1a4 4 0 0 0-4 4c0 3 4 8 4 8s4-5 4-8a4 4 0 0 0-4-4z" fill="none" stroke="#fff" stroke-width="1.4"/><circle cx="6" cy="5" r="1.4" fill="#fff"/></svg>
        </span>
        <span class="contact-text">Lindenweg 42b, 10115 Berlin,<br>Germany</span>
      </li>
      <li class="contact-item">
        <span class="contact-icon">
          <svg width="12" height="13" viewBox="0 0 12 13"><path d="M3 1l2 3-1.3 1.2c.6 1.5 1.7 2.7 3.2 3.4L8 7.3l3 2-1 2.5C5 11.5 1 7 1 2z" fill="none" stroke="#fff" stroke-width="1.3" stroke-linejoin="round"/></svg>
        </span>
        <span class="contact-text">+49 30 12345678</span>
      </li>
      <li class="contact-item">
        <span class="contact-icon">
          <svg width="13" height="13" viewBox="0 0 13 13"><text x="6.5" y="10.5" text-anchor="middle" font-family="Arial, sans-serif" font-size="12" fill="#fff">@</text></svg>
        </span>
        <span class="contact-text">info@harrowgateproperty.com</span>
      </li>
      <li class="contact-item">
        <span class="contact-icon">
          <svg width="13" height="13" viewBox="0 0 13 13" fill="none" stroke="#fff" stroke-width="1.1"><circle cx="6.5" cy="6.5" r="5.3"/><ellipse cx="6.5" cy="6.5" rx="2.3" ry="5.3"/><path d="M1.2 6.5h10.6M2 3.8h9M2 9.2h9"/></svg>
        </span>
        <span class="contact-text web">www.harrowgateproperty.com</span>
      </li>
    </ul>
  </section>

  <section class="page cover-page" aria-label="Cover page">
    <svg class="cover-art" width="550" height="770" viewBox="0 0 550 770">
      <defs>
        <linearGradient id="buildingTones" x1="0" y1="0" x2="1" y2="0">
          <stop offset="0" stop-color="#6f7378"/>
          <stop offset="0.5" stop-color="#585d63"/>
          <stop offset="0.75" stop-color="#9fb2c9"/>
          <stop offset="1" stop-color="#d5dbe2"/>
        </linearGradient>
        <linearGradient id="panelShade" x1="0" y1="0" x2="0" y2="1">
          <stop offset="0" stop-color="#f7f7f7"/>
          <stop offset="1" stop-color="#e4e4e4"/>
        </linearGradient>
        <linearGradient id="blueSweep" x1="0" y1="0" x2="1" y2="1">
          <stop offset="0" stop-color="#0a5fb0"/>
          <stop offset="1" stop-color="var(--blue)"/>
        </linearGradient>
        <clipPath id="topCurve">
          <path d="M0 0H550V50C420 170 250 262 0 310Z"/>
        </clipPath>
      </defs>

      <rect class="cover-photo" width="550" height="770" fill="url(#buildingTones)" role="img" aria-label="Photo looking up at city apartment towers and skyscrapers against a blue sky"/>

      <path class="top-band" d="M0 0H550V50C420 170 250 262 0 310Z" fill="url(#blueSweep)"/>
      <rect class="logo-panel" x="63" y="0" width="263" height="320" fill="url(#panelShade)" clip-path="url(#topCurve)"/>

      <path class="swoosh-white" d="M0 560C170 600 360 590 550 520V560C370 628 170 640 0 612Z" fill="#ffffff"/>
      <path class="swoosh-black" d="M270 618C380 610 470 585 550 552V582C470 612 380 628 270 628Z" fill="#111111"/>
      <path class="orange-base" d="M0 612C170 640 370 628 550 560V770H0Z" fill="var(--orange)"/>

      <rect class="side-strip" x="0" y="0" width="63" height="770" fill="#e6f0fa" opacity="0.4"/>

      <g class="headline">
        <text x="230" y="581">Creative</text>
        <text x="98" y="619">Solutions</text>
        <text class="connector" x="242" y="643">to all their</text>
        <text x="78" y="683">Real Estate</text>
        <text x="312" y="722">Needs</text>
      </g>
    </svg>

    <div class="brand cover-brand">
      <span class="brand-mark"></span>
      <span class="brand-name">
        <span class="line-main">Harrowgate</span>
        <span class="line-sub">Property Services</span>
      </span>
    </div>
  </section>

</main>
</body>
</html>
```